Copperwell Mini Storage - Ad for half Page

Need half page ad for a publication.
would also like to be able to use in the future
self storage facility - 3 locations, the third opening soon
do not like real busy projects...i have a logo but willing to tweak if needed

```html
<!DOCTYPE html>
<html lang="en">
<head>
<meta charset="utf-8">
<title>Copperwell Mini Storage – Half Page Ad</title>
<link href="https://fonts.googleapis.com/css2?family=Jost:wght@500;600;700&family=Montserrat:wght@500;600;700&display=swap" rel="stylesheet">
<style>
  :root{
    --page:#e9e9ea;
    --paper:#ffffff;
    --brown-dark:#5a2d0c;
    --copper:#c08a4e;
    --copper-bar:#9b5f18;
    --ink:#2b1a0e;
    --photo-cool:#c6d1dc;
    --photo-warm:#cdbfab;
  }
  *{box-sizing:border-box;margin:0;padding:0}
  html,body{width:800px;height:1200px;overflow:hidden;background:var(--page)}
  ul{list-style:none}
  .ad{
    position:absolute;left:20px;top:328px;width:760px;height:543px;
    background:var(--paper);overflow:hidden;
    font-family:"Montserrat",sans-serif;color:var(--ink);
    box-shadow:0 4px 14px rgba(0,0,0,.12);
  }
  .facility-photo{
    position:absolute;left:300px;top:0;width:460px;height:431px;
    background:linear-gradient(160deg,var(--photo-cool) 0%,var(--photo-warm) 100%);
  }
  .facility-photo::after{
    content:"";position:absolute;inset:0;
    background:linear-gradient(90deg,var(--paper) 0%,rgba(255,255,255,.85) 22%,rgba(255,255,255,0) 55%);
  }
  .brand{position:absolute;left:34px;top:37px;display:flex;align-items:center;gap:14px}
  .brand-square{width:55px;height:55px;background:var(--brown-dark)}
  .brand-name{font-family:"Jost",sans-serif;font-weight:700;font-size:27px;line-height:1.05;color:var(--brown-dark)}
  .headline{position:absolute;left:33px;top:119px;font-family:"Jost",sans-serif;font-weight:700;line-height:1}
  .headline .lead{display:block;font-size:30px;color:var(--brown-dark);letter-spacing:-.3px}
  .headline .main{display:block;font-size:44px;color:var(--copper);margin-top:2px;letter-spacing:-.3px}
  .divider{position:absolute;left:33px;top:204px;width:316px;height:1px;background:#bdb3aa}
  .divider::before{content:"";position:absolute;left:22px;top:-2px;width:44px;height:5px;border-radius:3px;background:var(--brown-dark)}
  .tagline{position:absolute;left:33px;top:224px;width:320px;font-weight:700;font-size:16px;line-height:1.3;color:var(--ink)}
  .banner{
    position:absolute;left:33px;top:279px;width:232px;height:25px;
    background:var(--copper);border-radius:0 13px 13px 0;
    font-family:"Jost",sans-serif;font-weight:600;font-size:13px;color:#fff;
    padding-left:16px;line-height:25px;
  }
  .features{position:absolute;left:33px;top:320px;display:grid;grid-template-columns:166px 180px;row-gap:8px}
  .feature{display:flex;align-items:center;gap:9px;font-weight:500;font-size:12.3px;line-height:1.25;color:var(--ink)}
  .feature svg{flex:none;width:44px;height:44px}
  .locations{position:absolute;left:384px;top:317px;display:flex;gap:24px}
  .location{
    width:96px;height:96px;border-radius:50%;background:var(--copper);
    border:3px solid #fff;box-shadow:0 2px 5px rgba(0,0,0,.25);
    display:flex;flex-direction:column;align-items:center;justify-content:center;
    text-align:center;color:#fff;
  }
  .location svg{width:11px;height:14px;margin-bottom:2px}
  .location .city{font-weight:700;font-size:12px;line-height:1.15;letter-spacing:.4px}
  .location .addr{font-size:7.5px;font-weight:500;line-height:1.3;margin-top:2px}
  .footer-square{position:absolute;left:0;top:436px;width:104px;height:107px;background:var(--brown-dark)}
  .contact-bar{
    position:absolute;left:114px;top:436px;width:646px;height:107px;background:var(--copper-bar);
    display:flex;align-items:center;padding-left:27px;gap:28px;color:#fff;
  }
  .contact-col{display:flex;flex-direction:column;gap:8px}
  .contact-line{display:flex;align-items:center;gap:9px}
  .contact-line svg{width:18px;height:18px;flex:none}
  .phone{font-weight:500;font-size:25px;letter-spacing:.4px;line-height:1.15}
  .web{font-weight:500;font-size:18px;line-height:1.5}
</style>
</head>
<body>
<main class="ad">
  <div class="facility-photo" role="img" aria-label="Photo of the storage facility office building and storage units"></div>

  <div class="brand">
    <div class="brand-square"></div>
    <div class="brand-name">Copperwell<br>Mini Storage</div>
  </div>

  <h1 class="headline">
    <span class="lead">SECURE, CONVENIENT</span>
    <span class="main">SELF-STORAGE</span>
  </h1>
  <div class="divider"></div>

  <p class="tagline">We are here to help with any of your storage needs, 24/7 Gate access.</p>

  <div class="banner">COPPERWELL MINI STORAGE</div>

  <ul class="features">
    <li class="feature">
      <svg viewBox="0 0 45 45"><circle cx="22.5" cy="22.5" r="21" fill="none" stroke="#5a2d0c" stroke-width="1.5" stroke-dasharray="2 2"/><circle cx="22.5" cy="22.5" r="17" fill="#fff" stroke="#5a2d0c" stroke-width="3"/><path d="M14 21 L22.5 15 L31 21 V30 H14Z" fill="#c08a4e"/><path d="M17 23h11M17 25.5h11M17 28h11" stroke="#fff" stroke-width="1"/></svg>
      <span>Climate<br>Controlled Units</span>
    </li>
    <li class="feature">
      <svg viewBox="0 0 45 45"><circle cx="22.5" cy="22.5" r="21" fill="none" stroke="#5a2d0c" stroke-width="1.5" stroke-dasharray="2 2"/><circle cx="22.5" cy="22.5" r="17" fill="#fff" stroke="#5a2d0c" stroke-width="3"/><path d="M13 21 L22.5 15 L32 21 V30 H13Z" fill="#c08a4e"/><rect x="16" y="23" width="13" height="5" fill="#fff"/></svg>
      <span>Boat and RV<br>Storage</span>
    </li>
    <li class="feature">
      <svg viewBox="0 0 45 45"><circle cx="22.5" cy="22.5" r="21" fill="none" stroke="#5a2d0c" stroke-width="1.5" stroke-dasharray="2 2"/><circle cx="22.5" cy="22.5" r="17" fill="#fff" stroke="#5a2d0c" stroke-width="3"/><path d="M14 21 L22.5 15 L31 21 V30 H14Z" fill="#c08a4e"/><rect x="17.5" y="23" width="10" height="7" fill="#fff"/></svg>
      <span>Non-Climate<br>Controlled Units</span>
    </li>
    <li class="feature">
      <svg viewBox="0 0 45 45"><circle cx="22.5" cy="22.5" r="21" fill="none" stroke="#5a2d0c" stroke-width="1.5" stroke-dasharray="2 2"/><circle cx="22.5" cy="22.5" r="17" fill="#fff" stroke="#5a2d0c" stroke-width="3"/><path d="M14 21 L22.5 15 L31 21 V30 H14Z" fill="#c08a4e"/><rect x="17" y="23" width="4" height="3" fill="#fff"/><rect x="23" y="23" width="4" height="3" fill="#fff"/><rect x="17" y="27" width="10" height="3" fill="#fff"/></svg>
      <span>Office and<br>Warehouse Space</span>
    </li>
  </ul>

  <div class="locations">
    <div class="location">
      <svg viewBox="0 0 11 14"><path d="M5.5 0A5 5 0 0 0 .5 5c0 3.5 5 9 5 9s5-5.5 5-9a5 5 0 0 0-5-5z" fill="#fff"/><circle cx="5.5" cy="5" r="2" fill="#c08a4e"/></svg>
      <span class="city">SAN<br>ANTONIO</span>
      <span class="addr">4120 Ridge Road<br>SAT, 78260</span>
    </div>
    <div class="location">
      <svg viewBox="0 0 11 14"><path d="M5.5 0A5 5 0 0 0 .5 5c0 3.5 5 9 5 9s5-5.5 5-9a5 5 0 0 0-5-5z" fill="#fff"/><circle cx="5.5" cy="5" r="2" fill="#c08a4e"/></svg>
      <span class="city">NEW<br>BRAUNFELS</span>
      <span class="addr">75 Mill Street<br>NB, TX 78132</span>
    </div>
    <div class="location">
      <span class="city">OPENING<br>SOON!</span>
      <span class="addr">Converse,<br>Texas</span>
    </div>
  </div>

  <div class="footer-square"></div>
  <div class="contact-bar">
    <div class="contact-col">
      <div class="contact-line">
        <svg viewBox="0 0 24 24"><path d="M6.6 10.8a15 15 0 0 0 6.6 6.6l2.2-2.2c.3-.3.7-.4 1-.2 1.1.4 2.3.6 3.6.6.6 0 1 .4 1 1V20c0 .6-.4 1-1 1A17 17 0 0 1 3 4c0-.6.4-1 1-1h3.5c.6 0 1 .4 1 1 0 1.3.2 2.5.6 3.6.1.3 0 .7-.2 1z" fill="#fff"/></svg>
        <span class="phone">(210) 555-0142</span>
      </div>
      <div class="contact-line">
        <svg viewBox="0 0 24 24"><path d="M6.6 10.8a15 15 0 0 0 6.6 6.6l2.2-2.2c.3-.3.7-.4 1-.2 1.1.4 2.3.6 3.6.6.6 0 1 .4 1 1V20c0 .6-.4 1-1 1A17 17 0 0 1 3 4c0-.6.4-1 1-1h3.5c.6 0 1 .4 1 1 0 1.3.2 2.5.6 3.6.1.3 0 .7-.2 1z" fill="#fff"/></svg>
        <span class="phone">(830) 555-0187</span>
      </div>
    </div>
    <div class="contact-col">
      <div class="contact-line">
        <svg viewBox="0 0 24 24"><rect x="2" y="5" width="20" height="14" fill="#fff"/><path d="M2 5l10 8 10-8" fill="none" stroke="#9b5f18" stroke-width="1.6"/></svg>
        <span class="web">sales@copperwellstorage.com</span>
      </div>
      <div class="contact-line">
        <svg viewBox="0 0 24 24" fill="none" stroke="#fff" stroke-width="1.6"><circle cx="12" cy="12" r="9.5"/><ellipse cx="12" cy="12" rx="4.5" ry="9.5"/><path d="M2.5 12h19M4 7h16M4 17h16"/></svg>
        <span class="web">www.copperwellstorage.com</span>
      </div>
    </div>
  </div>
</main>
</body>
</html>
```